TMAF inc Business Card Design

I have a rough draft of the TMAF inc logo that I would like to use on the business card. I also attached our logo for Brindlequay.com. I also included a sample of a business card from another mortgage company that I like. We would like a tagline on the back to say "let's get started" and below Brindlequay.com
Industry/Entity Type
Business
Contact Information for Business Card
Tallvane Mortgage and Funding, inc
Dale Fenwick
Mortgage Specialist
Direct (555)214-7093
Cell (555)608-1547
Fax (555)930-2861
dale@brindlequay.com
Westmarch Office of Land Registry 04728316
QFRB 417305

```html
<!DOCTYPE html>
<html lang="en">
<head>
<meta charset="utf-8">
<title>TMAF inc Business Card</title>
<link rel="stylesheet" href="https://fonts.googleapis.com/css2?family=Cinzel:wght@400;600&family=Questrial&display=swap">
<style>
  :root {
    --bg: #1c1c1e;
    --navy: #1c1a5e;
    --navy-deep: #12104a;
    --green: #6f9a2e;
    --grey-text: #5a5a5a;
    --rule: #c9c9c9;
    --card-white: #ffffff;
    --back-text: #e6e6ee;
  }
  html, body {
    margin: 0;
    padding: 0;
    width: 1200px;
    height: 871px;
    overflow: hidden;
    background: var(--bg);
  }
  .stage {
    position: relative;
    width: 1200px;
    height: 871px;
  }
  .card {
    position: absolute;
    left: 285px;
    width: 630px;
    height: 360px;
    box-sizing: border-box;
  }
  .card-back {
    top: 40px;
    background: linear-gradient(135deg, var(--navy) 0%, var(--navy-deep) 100%);
    overflow: hidden;
  }
  .back-mark {
    position: absolute;
    left: -60px;
    top: 150px;
    width: 230px;
    height: 230px;
    border-radius: 50%;
    border: 14px solid rgba(255,255,255,0.08);
    box-sizing: border-box;
  }
  .back-text {
    position: absolute;
    left: 0;
    right: 0;
    top: 150px;
    text-align: center;
    margin: 0;
  }
  .tagline {
    display: block;
    font-family: "Cinzel", serif;
    font-size: 24px;
    letter-spacing: 5px;
    color: var(--back-text);
    line-height: 1.2;
  }
  .back-site {
    display: block;
    margin-top: 14px;
    font-family: "Questrial", sans-serif;
    font-size: 14px;
    letter-spacing: 3px;
    color: var(--back-text);
    opacity: 0.85;
  }
  .card-front {
    top: 470px;
    background: var(--card-white);
  }
  .brand {
    position: absolute;
    left: 36px;
    top: 30px;
    display: flex;
    align-items: center;
    gap: 14px;
  }
  .brand-dot {
    width: 46px;
    height: 46px;
    border-radius: 50%;
    background: var(--navy);
  }
  .brand-name {
    font-family: "Cinzel", serif;
    font-weight: 600;
    font-size: 22px;
    letter-spacing: 2px;
    color: var(--navy);
    line-height: 1;
  }
  .brand-legal {
    font-family: "Cinzel", serif;
    font-size: 7px;
    letter-spacing: 0.5px;
    color: var(--green);
    margin-top: 5px;
  }
  .rule {
    position: absolute;
    height: 1px;
    background: var(--rule);
  }
  .rule-top { left: 36px; width: 300px; top: 96px; }
  .rule-contact { left: 330px; width: 270px; top: 170px; }
  .person {
    position: absolute;
    left: 36px;
    top: 112px;
  }
  .person-name {
    font-family: "Cinzel", serif;
    font-size: 19px;
    letter-spacing: 2px;
    color: #1b1b2e;
  }
  .person-title {
    font-family: "Questrial", sans-serif;
    font-size: 12px;
    letter-spacing: 2px;
    color: var(--green);
    margin-top: 4px;
  }
  .contact {
    position: absolute;
    left: 330px;
    top: 182px;
    font-family: "Questrial", sans-serif;
    font-size: 14px;
    letter-spacing: 2px;
    color: var(--grey-text);
  }
  .contact-row {
    display: flex;
    align-items: center;
    gap: 14px;
    height: 21px;
  }
  .contact-row svg {
    width: 14px;
    height: 14px;
    fill: none;
    stroke: var(--navy);
    stroke-width: 1.6;
  }
  .registry {
    margin-top: 6px;
    line-height: 21px;
  }
</style>
</head>
<body>
<main class="stage">
  <section class="card card-back" aria-label="Card back">
    <div class="back-mark" aria-hidden="true"></div>
    <p class="back-text">
      <span class="tagline">LET'S GET STARTED</span>
      <span class="back-site">Brindlequay.com</span>
    </p>
  </section>

  <section class="card card-front" aria-label="Card front">
    <div class="brand">
      <div class="brand-dot" aria-hidden="true"></div>
      <div>
        <div class="brand-name">TMAF INC</div>
        <div class="brand-legal">Tallvane Mortgage and Funding, inc</div>
      </div>
    </div>
    <div class="rule rule-top"></div>

    <div class="person">
      <div class="person-name">DALE FENWICK</div>
      <div class="person-title">Mortgage Specialist</div>
    </div>

    <div class="rule rule-contact"></div>
    <div class="contact">
      <div class="contact-row">
        <svg viewBox="0 0 16 16"><path d="M2 6 Q8 1 14 6 L12 8 L10 6.5 L6 6.5 L4 8 Z"/><rect x="4" y="9" width="8" height="5"/></svg>
        <span>(555)214-7093</span>
      </div>
      <div class="contact-row">
        <svg viewBox="0 0 16 16"><rect x="4.5" y="1.5" width="7" height="13" rx="1.5"/><line x1="7" y1="12" x2="9" y2="12"/></svg>
        <span>(555)608-1547</span>
      </div>
      <div class="contact-row">
        <svg viewBox="0 0 16 16"><rect x="4" y="2" width="8" height="4"/><rect x="2" y="6" width="12" height="6"/><rect x="4" y="10" width="8" height="4"/></svg>
        <span>(555)930-2861</span>
      </div>
      <div class="contact-row">
        <svg viewBox="0 0 16 16"><rect x="1.5" y="3.5" width="13" height="9"/><path d="M1.5 3.5 L8 9 L14.5 3.5"/></svg>
        <span>dale@brindlequay.com</span>
      </div>
      <div class="registry">
        Westmarch Office<br>
        of Land Registry 04728316<br>
        QFRB 417305
      </div>
    </div>
  </section>
</main>
</body>
</html>
```